Accounting and Tax Professional

New business with a business model based on good service and bright staff,

Jordan Pike B.Com CPA DIRECTOR

"Kestrel Ledger Services Pty Ltd"
ABN 47 382 615 908

Registered Tax Agent
PROFESSIONAL PERSONABLE TIMELY OR "PROFESSIONAL ADVICE TAILORED TO SUIT YOU"
Superannuation|Business services|Management consulting|Taxation|Software support
E Jordan@KestrelLedgerServices.Com.au
WWW.KESTRELLEDGERSERVICES.COM.AU
Phone: +61 0488 517 934
23460 Marlow Valley Road Fernside QLD 4367, Australia

hi, I have uploaded an .EPS logo as requested by one of the designers, let me know if this is not the right size for the business card. thanks Jordan

Target Market(s)

Mainly Business clients

Industry/Entity Type

Business

Font styles to use
Serif

Colors
85acd3
3377b5

Requirements
Must have
• clean/crisp/well laid out

```html
<!DOCTYPE html>
<html lang="en">
<head>
<meta charset="utf-8">
<title>Kestrel Ledger Services – Business Card</title>
<link href="https://fonts.googleapis.com/css2?family=Montserrat:wght@500;600&family=Lato:wght@400;700&display=swap" rel="stylesheet">
<style>
  :root {
    --backdrop: #e4e5e7;
    --card: #ffffff;
    --brand-blue: #7e9abb;
    --brand-blue-deep: #3377b5;
    --soft-grey: #cfd0d3;
    --ink: #1f2328;
    --ink-soft: #4a4f57;
  }
  * { box-sizing: border-box; margin: 0; padding: 0; }
  html, body { width: 1200px; height: 772px; overflow: hidden; }
  body {
    background: var(--backdrop);
    display: flex;
    align-items: center;
    justify-content: center;
    gap: 40px;
    font-family: "Lato", sans-serif;
    color: var(--ink);
  }
  .card {
    position: relative;
    width: 540px;
    height: 309px;
    background: var(--card);
    box-shadow: 0 6px 18px rgba(0,0,0,0.18);
    overflow: hidden;
  }
  .card-bands { position: absolute; inset: 0; }

  .wordmark { display: flex; align-items: center; gap: 12px; }
  .wordmark-dot {
    width: 46px; height: 46px; border-radius: 50%;
    background: var(--brand-blue);
    flex: none;
  }
  .wordmark-text {
    font-family: "Montserrat", sans-serif;
    font-weight: 500;
    color: var(--ink);
    line-height: 1;
  }
  .wordmark-name { font-size: 40px; letter-spacing: 2px; }
  .wordmark-sub { font-size: 9.5px; letter-spacing: 0.6px; margin-top: 5px; }

  /* front */
  .card-front .wordmark { position: absolute; left: 176px; top: 44px; }
  .contact-list {
    position: absolute; right: 22px; top: 126px;
    list-style: none;
    font-size: 10.5px;
    color: var(--ink-soft);
  }
  .contact-address { margin-bottom: 12px; line-height: 1.35; }
  .contact-item { display: flex; align-items: center; gap: 7px; margin-bottom: 6px; }
  .contact-icon { width: 11px; height: 11px; fill: var(--brand-blue); flex: none; }
  .holder {
    position: absolute; left: 120px; bottom: 18px;
    color: #fff;
  }
  .holder-name { font-size: 13px; font-weight: 700; letter-spacing: 1.5px; white-space: nowrap; }
  .holder-role { font-size: 10px; margin-top: 3px; letter-spacing: 0.5px; }

  /* back */
  .card-back { display: flex; align-items: center; justify-content: center; }
  .card-back .wordmark-dot { width: 62px; height: 62px; }
  .card-back .wordmark-name { font-size: 52px; }
  .card-back .wordmark-sub { font-size: 12px; }
</style>
</head>
<body>

  <section class="card card-back" aria-label="Card back">
    <div class="wordmark">
      <span class="wordmark-dot"></span>
      <div class="wordmark-text">
        <div class="wordmark-name">KESTREL</div>
        <div class="wordmark-sub">LEDGER SERVICES PTY LTD</div>
      </div>
    </div>
  </section>

  <section class="card card-front" aria-label="Card front">
    <svg class="card-bands" viewBox="0 0 540 309" aria-hidden="true">
      <path d="M0,20 C110,130 250,240 420,309" fill="none" stroke="var(--soft-grey)" stroke-width="10"/>
      <path d="M0,70 C100,170 220,260 380,309 L0,309 Z" fill="var(--brand-blue)"/>
    </svg>

    <div class="wordmark">
      <span class="wordmark-dot"></span>
      <div class="wordmark-text">
        <div class="wordmark-name">KESTREL</div>
        <div class="wordmark-sub">LEDGER SERVICES PTY LTD</div>
      </div>
    </div>

    <ul class="contact-list">
      <li class="contact-address">23460 Marlow Valley Road<br>Fernside QLD 4367</li>
      <li class="contact-item">
        <svg class="contact-icon" viewBox="0 0 24 24"><path d="M6.6 10.8a15 15 0 0 0 6.6 6.6l2.2-2.2c.3-.3.7-.4 1-.2 1.1.4 2.3.6 3.6.6.6 0 1 .4 1 1V20c0 .6-.4 1-1 1A17 17 0 0 1 3 4c0-.6.4-1 1-1h3.5c.6 0 1 .4 1 1 0 1.3.2 2.5.6 3.6.1.3 0 .7-.2 1z"/></svg>
        +61 0488 517 934
      </li>
      <li class="contact-item">
        <svg class="contact-icon" viewBox="0 0 24 24"><path d="M2 5h20v14H2z M2 5l10 8 10-8" fill="none" stroke="var(--brand-blue)" stroke-width="2.4"/></svg>
        Jordan@KestrelLedgerServices.Com.au
      </li>
      <li class="contact-item">
        <svg class="contact-icon" viewBox="0 0 24 24"><circle cx="12" cy="12" r="10"/></svg>
        WWW.KESTRELLEDGERSERVICES.COM.AU
      </li>
    </ul>

    <div class="holder">
      <div class="holder-name">JORDAN PIKE</div>
      <div class="holder-role">Director</div>
    </div>
  </section>

</body>
</html>
```